Business Cards

Simple but professional looking business cards

Name: Rina Toskovar
Title: Principle Enterprise Applications Consultant
Email: r@kldo.net.au
web : www.kldo.net.au
Phone: +61.8.92315547
Mobile: +61.438516622

Hi All, Please include the office address Level 1, 100 Bramwell St, Norvale Heights, WA, 6091

```html
<!DOCTYPE html>
<html lang="en">
<head>
<meta charset="utf-8">
<title>KLDO Business Cards</title>
<link rel="stylesheet" href="https://fonts.googleapis.com/css2?family=Tinos:wght@400;700&display=swap">
<style>
  :root {
    --bg: #d9d9d9;
    --card-white: #f7f7f5;
    --brand-blue: #1b5aa6;
    --brand-blue-deep: #0e3f86;
    --brand-blue-light: #1f6cc0;
    --brand-green: #7cbf2a;
    --badge-dark: #1a1a1a;
    --badge-light: #ffffff;
    --ink: #1d56a0;
  }
  * { margin: 0; padding: 0; box-sizing: border-box; }
  html, body { width: 1200px; height: 1000px; overflow: hidden; }
  body {
    background: var(--bg);
    font-family: "Tinos", "Times New Roman", serif;
    position: relative;
  }
  .card {
    position: absolute;
    width: 720px;
    height: 410px;
    border-radius: 4px;
    box-shadow: 0 6px 18px rgba(0,0,0,0.18);
    overflow: hidden;
  }

  /* Back of card */
  .card-back {
    left: 420px;
    top: 50px;
    background: radial-gradient(ellipse at 45% 40%, var(--brand-blue-light) 0%, var(--brand-blue) 45%, var(--brand-blue-deep) 100%);
  }
  .card-back .wordmark {
    position: absolute;
    left: 0; right: 0; top: 145px;
    justify-content: center;
    color: var(--badge-light);
  }
  .card-back .partner-badge {
    position: absolute;
    right: 30px; top: 34px;
    width: 130px; height: 40px;
    background: var(--badge-light);
  }

  /* Wordmark */
  .wordmark {
    display: flex;
    align-items: center;
    gap: 18px;
    font-weight: 700;
    font-size: 120px;
    line-height: 1;
    letter-spacing: 6px;
  }
  .wordmark .dot {
    width: 34px; height: 34px;
    border-radius: 50%;
    background: currentColor;
    flex: none;
  }

  /* Front of card */
  .card-front {
    left: 80px;
    top: 520px;
    background: var(--card-white);
    color: var(--ink);
  }
  .card-front .wordmark {
    position: absolute;
    left: 40px; top: 28px;
    font-size: 140px;
    letter-spacing: 10px;
    color: var(--brand-blue);
  }
  .card-front .wordmark .dot { background: var(--brand-green); }
  .identity {
    position: absolute;
    left: 40px; top: 190px;
  }
  .identity .name {
    font-size: 28px;
    font-weight: 700;
    letter-spacing: 0.5px;
  }
  .identity .role {
    font-size: 18px;
    margin-top: 4px;
  }
  .card-front .partner-badge {
    position: absolute;
    left: 40px; top: 282px;
    width: 150px; height: 44px;
    background: var(--badge-dark);
  }
  .contact {
    position: absolute;
    right: 36px; top: 250px;
    list-style: none;
    font-size: 20px;
    line-height: 1.3;
  }
  .office {
    position: absolute;
    left: 130px; top: 362px;
    font-size: 20px;
  }
</style>
</head>
<body>
  <section class="card card-back">
    <div class="wordmark"><span class="dot"></span>KLDO</div>
    <div class="partner-badge" role="img" aria-label="Partner badge"></div>
  </section>

  <section class="card card-front">
    <div class="wordmark"><span class="dot"></span>KLDO</div>
    <div class="identity">
      <p class="name">Rina Toskovar</p>
      <p class="role">Principle Enterprise Applications Consultant</p>
    </div>
    <div class="partner-badge" role="img" aria-label="Partner badge"></div>
    <ul class="contact">
      <li>Email : r@kldo.net.au</li>
      <li>web : www.kldo.net.au</li>
      <li>Phone : +61.8.92315547</li>
      <li>Mobile : +61.438516622</li>
    </ul>
    <p class="office">Office : Level 1, 100 Bramwell St Norvale Heights, WA, 6091</p>
  </section>
</body>
</html>
```